依頼詳細
通常のチラシのイメージに近い形で、手書きのデータのデザインをもとに、シンプルかつインパクトの強いチラシにしたいと思います。

・いったん手書きのデータの内容を記載したデザインで採用を決定し、その上で細かな部分も完成させたデータの作成をお願いしたいと思います。
宜しくお願いします。
記載項目
添付のロゴをご使用ください。
通常のチラシデータも添付しています。
サイズ
A4
ページ数
片面
希望イメージ
シンプル 複雑
単色 カラフル
暗い 明るい
日常 高級
遊び心 厳粛
未来的 伝統的
女性的 男性的
希望する色
緑系、青系
納品ファイル
• 高解像度JPG (.jpg)
• イラストレーター形式 (.ai)
補足説明
ご提案頂きありがとうございます。
依頼の詳細が正しく伝えられていないかもしれません。

可能な限りシンプルなデザインで
30教室達成、3000名を強調するチラシにできればと考えています。

作成中の方はこの部分を考慮して頂ければと思います。
宜しくお願いします。
■ 選んだ理由

親しみのあるイメージを感じることができました。
母親・子どもたちに気に行っていただけるデザインだと思いました。

■ 提案者全員のお礼・コメント

たくさんの提案ありがとうございました。

```html
<!DOCTYPE html>
<html lang="ja">
<head>
<meta charset="UTF-8">
<title>個別指導そだち 特別キャンペーン</title>
<link href="https://fonts.googleapis.com/css2?family=M+PLUS+Rounded+1c:wght@500;800;900&family=Noto+Sans+JP:wght@700;900&display=swap" rel="stylesheet">
<style>
  :root{
    --green:#1f9a3c;
    --green-dark:#137a2b;
    --green-light:#8fd14f;
    --blue:#1d6fc4;
    --blue-dark:#0f4c91;
    --sky:#e6f4fc;
    --sky-deep:#bfe2f5;
    --red:#e0242b;
    --yellow:#ffe100;
    --ink:#1a1a1a;
    --white:#ffffff;
  }
  *{box-sizing:border-box;margin:0;padding:0}
  html,body{width:849px;height:1200px;overflow:hidden;background:var(--white)}
  body{font-family:"Noto Sans JP",sans-serif;color:var(--ink)}
  .flyer{position:relative;width:849px;height:1200px;overflow:hidden;background:var(--white)}

  .hero{position:absolute;left:0;top:0;width:849px;height:780px;
    background:radial-gradient(ellipse at 50% 50%, var(--sky) 0%, var(--sky) 40%, var(--sky-deep) 100%);}

  .brand{position:absolute;left:28px;top:18px;width:320px}
  .brand-name{display:flex;align-items:center;gap:12px;font-family:"M PLUS Rounded 1c",sans-serif;font-weight:900;color:var(--green);font-size:62px;line-height:1;letter-spacing:2px}
  .brand-mark{width:34px;height:34px;background:var(--green);border-radius:4px}
  .brand-sub{display:block;font-size:19px;letter-spacing:0}
  .brand-tagline{margin-top:12px;font-size:17px;font-weight:900;color:var(--ink);white-space:nowrap}

  .info-box{position:absolute;right:16px;top:16px;width:312px;border:3px solid var(--blue);background:var(--white);border-radius:6px;padding:10px 10px 0;text-align:center}
  .info-lead{font-size:12px;font-weight:700;color:var(--blue-dark)}
  .info-tags{display:flex;justify-content:center;gap:8px;margin-top:8px}
  .tag{background:var(--red);color:var(--white);font-size:19px;font-weight:900;padding:2px 10px;border-radius:3px}
  .info-note{font-size:21px;font-weight:900;color:var(--blue-dark);margin-top:6px}
  .info-grades{margin:8px -10px 0;background:var(--yellow);color:var(--red);font-size:22px;font-weight:900;padding:6px 0;border-radius:0 0 3px 3px}

  .region-ribbon{position:absolute;left:290px;top:208px;width:270px;height:40px;background:var(--blue);color:var(--white);font-size:22px;font-weight:900;text-align:center;line-height:40px;border-radius:4px;transform:rotate(-3deg)}
  .region-ribbon em{font-style:normal;color:var(--yellow);font-size:26px}

  .classrooms{position:absolute;left:240px;top:252px;width:360px;height:82px;display:flex;align-items:center;justify-content:center;gap:8px}
  .label-stack{background:var(--green);color:var(--white);font-size:20px;font-weight:900;line-height:1.05;padding:8px 6px;border-radius:6px;width:34px;text-align:center}
  .classrooms .num{font-family:"M PLUS Rounded 1c",sans-serif;font-weight:900;font-size:86px;color:var(--red);line-height:1}
  .classrooms .unit{font-size:44px;font-weight:900;color:var(--green-dark)}

  .achieved{position:absolute;left:604px;top:238px;width:104px;height:104px;border-radius:50%;background:var(--red);border:5px solid var(--white);color:var(--white);font-size:36px;font-weight:900;display:flex;align-items:center;justify-content:center;transform:rotate(12deg);box-shadow:0 3px 0 rgba(0,0,0,.15)}

  .students{position:absolute;left:195px;top:345px;width:470px;height:140px;display:flex;align-items:center;justify-content:center;gap:8px}
  .students .label-circle{width:70px;height:70px;border-radius:50%;background:var(--green);color:var(--white);font-size:20px;font-weight:900;line-height:1.05;display:flex;align-items:center;justify-content:center;text-align:center;flex-shrink:0}
  .students .num{font-family:"M PLUS Rounded 1c",sans-serif;font-weight:900;font-size:128px;letter-spacing:-2px;color:var(--red);line-height:1}
  .students .unit{font-size:56px;font-weight:900;color:var(--red);align-self:flex-end;margin-bottom:14px}

  .campaign-ribbon{position:absolute;left:232px;top:494px;width:390px;height:70px;background:var(--red);color:var(--white);font-size:44px;font-weight:900;text-align:center;line-height:70px;clip-path:polygon(0 0,100% 0,96% 50%,100% 100%,0 100%,4% 50%)}

  .figure{position:absolute;top:340px;width:180px;height:280px;border-radius:90px 90px 10px 10px;background:linear-gradient(180deg,#f6d7b8 0%,#2d4c8a 45%,#1c3566 100%)}
  .figure-left{left:40px}
  .figure-right{right:36px}

  .placeholder-line{position:absolute;left:0;width:849px;text-align:center;font-size:26px;letter-spacing:2px;color:var(--ink)}

  .offer{position:absolute;left:0;top:770px;width:849px;height:165px;background:var(--green)}
  .offer-box{position:absolute;left:34px;top:36px;width:781px;height:104px;background:var(--white);border-radius:10px;display:flex;align-items:center;justify-content:center;gap:22px}
  .offer-max{background:var(--green);color:var(--white);font-size:42px;font-weight:900;padding:0 14px;line-height:62px;border-radius:6px}
  .offer-term{font-size:68px;font-weight:900;color:var(--green-dark)}
  .offer-term small{font-size:48px}
  .offer-price{font-family:"M PLUS Rounded 1c",sans-serif;font-size:120px;font-weight:900;color:var(--red);line-height:1;margin-top:-14px}
  .offer-price small{font-family:"Noto Sans JP",sans-serif;font-size:56px}

  .details{position:absolute;left:40px;top:950px;width:769px;display:flex;gap:30px}
  .details-label{background:var(--green);color:var(--white);font-size:22px;font-weight:900;padding:6px 16px;border-radius:20px;height:42px;white-space:nowrap}
  .details-list{list-style:none;font-size:22px;line-height:46px;flex:1}
  .details-list li{border-bottom:2px dotted var(--green-light)}

  .bottom-band{position:absolute;left:0;top:1110px;width:849px;height:90px;background:var(--green-dark);display:flex;align-items:center;justify-content:center;gap:14px}
  .bottom-band .lead{color:var(--yellow);font-size:36px;font-weight:900}
  .bottom-band .text{color:var(--white);font-size:36px;font-weight:900}
  .bottom-band .highlight{background:var(--white);color:var(--red);font-size:42px;font-weight:900;padding:2px 18px;border-radius:6px}
</style>
</head>
<body>
<main class="flyer">
  <div class="hero"></div>

  <header class="brand">
    <div class="brand-name"><span class="brand-mark"></span><span><span class="brand-sub">個別指導</span>そだち</span></div>
    <p class="brand-tagline">面倒見No.1 成績保証の個別指導専門塾</p>
  </header>

  <aside class="info-box">
    <p class="info-lead">圧倒的な指導力と豊富な実績があるから</p>
    <div class="info-tags"><span class="tag">中学受験</span><span class="tag">私立中学生</span></div>
    <p class="info-note">にもしっかり対応!</p>
    <p class="info-grades">小・中・高・全学年指導</p>
  </aside>

  <div class="figure figure-left" role="img" aria-label="制服姿の男子生徒のイラスト"></div>
  <div class="figure figure-right" role="img" aria-label="制服姿の女子生徒のイラスト"></div>

  <p class="region-ribbon">南大阪<em>地域No.1</em>塾!</p>

  <div class="classrooms">
    <span class="label-stack">教室数</span>
    <span class="num">30</span>
    <span class="unit">教室</span>
  </div>

  <div class="achieved">達成</div>

  <div class="students">
    <span class="label-circle">生徒<br>数</span>
    <span class="num">3000</span>
    <span class="unit">名</span>
  </div>

  <p class="campaign-ribbon">特別キャンペーン</p>

  <p class="placeholder-line" style="top:628px">●●●●●●●●●●●●●●●●●</p>
  <p class="placeholder-line" style="top:680px">●●●●●●●●●●●●●●●●●</p>

  <section class="offer">
    <div class="offer-box">
      <span class="offer-max">最大</span>
      <span class="offer-term">3<small>ヶ月間</small></span>
      <span class="offer-price">0<small>円</small></span>
    </div>
  </section>

  <section class="details">
    <span class="details-label">キャンペーン内容</span>
    <ol class="details-list">
      <li>①●●●●●●●●●●●●●●●●●</li>
      <li>②●●●●●●●●●●●●●●●●●</li>
      <li>③●●●●●●●●●●●●●●●●●</li>
    </ol>
  </section>

  <footer class="bottom-band">
    <span class="lead">さらに</span>
    <span class="text">友達や兄弟入塾で</span>
    <span class="highlight">授業料半額</span>
  </footer>
</main>
</body>
</html>
```